Amber Hollow Cafe Business Card

We need a business card design for a new European Cafe. Main menu will be coffee and deserts.

Industry/Entity Type

Business

Requirements
Must have
• Logo - 1 of the attached versions
Address - TBA (you can use 123 Fake St Unit 1 for now)
Phone - TBA (you can use 555-013-2748 for now)

```html
<!DOCTYPE html>
<html lang="en">
<head>
<meta charset="utf-8">
<title>Amber Hollow Cafe – Business Card</title>
<link rel="stylesheet" href="https://fonts.googleapis.com/css2?family=Open+Sans:wght@400;700&display=swap">
<style>
  :root {
    --ink: #231f20;
    --accent: #a3272b;
    --text: #000000;
    --paper: #ffffff;
  }
  html, body {
    margin: 0;
    padding: 0;
    overflow: hidden;
    background: var(--paper);
  }
  .card {
    position: relative;
    width: 1200px;
    height: 693px;
    background: var(--paper);
    overflow: hidden;
    font-family: "Open Sans", Arial, sans-serif;
    color: var(--ink);
  }
  .brand-mark {
    position: absolute;
    left: 44px;
    top: 40px;
    width: 283px;
    height: 281px;
    background: var(--ink);
    border-radius: 8px;
  }
  .brand-name {
    position: absolute;
    left: 384px;
    top: 93px;
    width: 740px;
    margin: 0;
    font-weight: 400;
    color: var(--ink);
    text-align: center;
  }
  .brand-name .line {
    display: block;
    white-space: nowrap;
  }
  .brand-name .line--main {
    font-size: 108px;
    line-height: 115px;
    letter-spacing: -2px;
  }
  .brand-name .line--sub {
    font-size: 80px;
    line-height: 90px;
    letter-spacing: 3px;
  }
  .contact {
    position: absolute;
    right: 46px;
    top: 378px;
    margin: 0;
    text-align: right;
    font-style: normal;
    font-weight: 700;
    font-size: 50px;
    line-height: 71px;
  }
  .contact .line {
    display: block;
    white-space: nowrap;
  }
  .contact .person-name,
  .contact .person-role {
    color: var(--accent);
  }
  .contact .address,
  .contact .phone {
    color: var(--text);
  }
</style>
</head>
<body>
  <main class="card">
    <div class="brand-mark" aria-hidden="true"></div>
    <h1 class="brand-name">
      <span class="line line--main">Amber Hollow</span>
      <span class="line line--sub">Cafe</span>
    </h1>
    <address class="contact">
      <span class="line person-name">Daniel Reyes</span>
      <span class="line person-role">Manager</span>
      <span class="line address">48 Linden Row, Unit 3</span>
      <span class="line phone">555-013-2748</span>
    </address>
  </main>
</body>
</html>
```